Front and back label for Men’s Beard and Face Lotion

Slogan to include somewhere on the label: STAY WILD. STAY BEARDED.

We have created a men’s face and beard lotion for our company, Ridgefern Beard Company, a subsidiary of Kestrel Lather Co. we need new labels for our entire men’s grooming line but we’re starting with the face/beard lotion with the idea that the style of that label will be able to carry across to the beard balms, oils, etc. I’ll upload our temporary logo, but we have a logo designer working on our permanent logo right now, should have it in a couple of days.

For the size: 1.5in (38.1mm) wide x 2.5in (63.5mm) tall.

Bottle is a dark green rectangular pump bottle. Color scheme needs to not clash. I’ll upload an AI rendering to give more info, though whatever you come up with does not have to copy the rendering. It’s simply a style that I liked.

We don’t want to look too much like the other beard brands out there with their “refined vintage gentleman” look. We’re rough around the edges, very outdoorsman and mountain oriented. Bright colors used to draw attention is totally fine. Our name comes from the Sawtooth Mountains in Idaho, US.

Target Market(s)

Bearded Men ages 20-death. Also some appeal to their partners.

Industry/Entity Type

Cosmetics labels, hair and skincare

Requirements
Must have
• The URL : RidgefernBeard.example on the back label. A spot on the back for a UPC. Proper bleed layout for Corvane Label printing requirements.
Nice to have
• A design that we can hire the designer to base other product designs off of. A foundation-design vibe, in a sense. This project could lead to 10 more designs already planned.
Should not have
• Pink, purple, too generic of a beard vibe. We want this to look Cool.

```html
<!DOCTYPE html>
<html lang="en">
<head>
<meta charset="utf-8">
<title>Ridgefern Face &amp; Beard Lotion – Label Concept</title>
<link rel="stylesheet" href="https://fonts.googleapis.com/css2?family=Oswald:wght@500;600;700&family=Arimo:wght@400;700&display=swap">
<style>
  :root {
    --pine: #173a30;
    --pine-deep: #10291f;
    --bone: #f3ead8;
    --blaze: #f27a33;
    --paper: #f8f6f1;
    --ink: #111111;
    --muted: #6f7470;
    --stage: #bdb9b4;
    --display: "Oswald", "Arial Narrow", sans-serif;
    --body: "Arimo", "Helvetica Neue", Arial, sans-serif;
  }
  * { box-sizing: border-box; margin: 0; padding: 0; }
  html, body { width: 859px; height: 1200px; overflow: hidden; }
  body { background: var(--paper); font-family: var(--body); position: relative; }

  .stage { position: absolute; left: 0; top: 0; width: 859px; height: 573px; background: var(--stage); }
  .stage-slot { position: absolute; top: 176px; width: 173px; height: 289px; }
  .stage-slot .label { transform: scale(0.74); transform-origin: 0 0; }
  .stage-slot.front-slot { left: 175px; }
  .stage-slot.back-slot { left: 472px; }

  /* Label: 1.5 x 2.5 in */
  .label { position: relative; width: 234px; height: 390px; overflow: hidden; }
  .label-top-bar { position: absolute; left: 0; top: 0; width: 100%; height: 7px; background: var(--blaze); }

  .label-front { background: var(--pine); color: var(--bone); text-align: center; }
  .front-art { position: absolute; left: 13px; top: 20px; width: 208px; height: 84px;
    background: linear-gradient(180deg, #d9d6cc 0%, #7f8580 45%, #2a3b33 80%, var(--pine) 100%);
    border-radius: 40% 40% 4px 4px / 60% 60% 4px 4px; }
  .brand-name { position: absolute; left: 10px; right: 10px; top: 104px;
    font-family: var(--display); font-weight: 700; font-size: 19px; line-height: 20px;
    letter-spacing: 1.5px; color: var(--bone); text-transform: uppercase; }
  .product-kicker { position: absolute; left: 0; right: 0; top: 146px;
    font-family: var(--display); font-weight: 600; font-size: 30px; line-height: 34px; letter-spacing: 1px; }
  .product-name { position: absolute; left: 0; right: 0; top: 174px;
    font-family: var(--display); font-weight: 500; font-size: 66px; line-height: 76px; letter-spacing: 1px; }
  .variant-band { position: absolute; left: 0; top: 250px; width: 100%; height: 31px; background: var(--blaze);
    font-family: var(--display); font-weight: 600; font-size: 19px; line-height: 31px; letter-spacing: 4px; color: var(--pine-deep); }
  .key-ingredients { position: absolute; left: 0; right: 0; top: 285px;
    font-family: var(--display); font-weight: 500; font-size: 14px; line-height: 16px; letter-spacing: 0.4px; }
  .slogan { position: absolute; left: 0; right: 0; top: 318px; color: var(--blaze);
    font-family: var(--display); font-weight: 600; font-size: 18px; line-height: 20px; letter-spacing: 1px; }
  .net-contents { position: absolute; left: 0; right: 0; top: 363px; font-size: 13px; line-height: 16px; }

  .label-back { background: var(--bone); color: var(--ink); border: 1px solid #e3d8c2; }
  .back-title { position: absolute; left: 15px; top: 15px;
    font-family: var(--display); font-weight: 600; font-size: 20px; line-height: 24px; color: var(--pine); letter-spacing: 0.3px; }
  .back-rule { position: absolute; left: 15px; right: 15px; top: 42px; height: 2px; background: var(--blaze); }
  .back-copy { position: absolute; left: 15px; right: 8px; top: 47px; font-size: 11.6px; line-height: 13.7px; }
  .back-heading { font-weight: 700; font-size: 12.5px; letter-spacing: 1px; line-height: 15px; }
  .back-heading + p { margin-bottom: 2px; }
  .maker { position: absolute; left: 0; right: 0; top: 211px; text-align: center; font-weight: 700; font-size: 11.6px; }
  .upc-area { position: absolute; left: 14px; right: 14px; top: 231px; height: 128px; background: #ffffff;
    display: flex; flex-direction: column; align-items: center; justify-content: center; gap: 8px; color: var(--muted); }
  .upc-area strong { font-size: 14px; letter-spacing: 2px; }
  .upc-area span { font-size: 11px; letter-spacing: 0.5px; }
  .web-address { position: absolute; left: 0; right: 0; top: 362px; text-align: center; font-weight: 700; font-size: 13.5px; }

  /* Presentation sheet */
  .accent-bar { position: absolute; left: 43px; top: 610px; width: 7px; height: 44px; background: var(--blaze); }
  .sheet-title { position: absolute; left: 64px; top: 608px; font-weight: 700; font-size: 28px; line-height: 32px; color: var(--pine); letter-spacing: 0.5px; }
  .sheet-subtitle { position: absolute; left: 65px; top: 643px; font-size: 10px; color: var(--muted); letter-spacing: 0.2px; }
  .view-tag { position: absolute; top: 687px; font-size: 8.5px; font-weight: 700; color: #4c524e; letter-spacing: 0.3px; }
  .sheet-label { position: absolute; top: 708px; }
  .size-note { position: absolute; top: 1107px; font-size: 8px; color: var(--muted); }
  .col-front { left: 61px; }
  .col-back { left: 332px; }

  .notes { position: absolute; left: 619px; top: 620px; width: 200px; color: #555a56; }
  .note-heading { font-size: 10.5px; font-weight: 700; color: var(--pine); letter-spacing: 0.2px; margin-bottom: 8px; }
  .note-body { font-size: 9px; line-height: 14px; }
  .note-list { list-style: none; font-size: 9px; line-height: 15px; }
  .palette { position: absolute; left: 619px; top: 1084px; display: flex; gap: 17px; }
  .swatch { width: 43px; height: 18px; }
  .swatch.pine { background: var(--pine); }
  .swatch.bone { background: var(--bone); border: 1px solid #e3d8c2; }
  .swatch.blaze { background: var(--blaze); }
  .footer-rule { position: absolute; left: 43px; top: 1158px; width: 773px; height: 1px; background: #dedbd4; }
</style>
</head>
<body>

<section class="stage" aria-label="Front and back labels, flat">
  <div class="stage-slot front-slot">
    <div class="label label-front">
      <div class="label-top-bar"></div>
      <div class="front-art" role="img" aria-label="Illustration of jagged snowy mountain peaks with pine forest"></div>
      <div class="brand-name">Ridgefern<br>Beard Company</div>
      <div class="product-kicker">FACE &amp; BEARD</div>
      <div class="product-name">LOTION</div>
      <div class="variant-band">UNSCENTED</div>
      <div class="key-ingredients">ALOE VERA + NIACINAMIDE<br>+ ARGAN OIL</div>
      <div class="slogan">STAY WILD.<br>STAY BEARDED.</div>
      <div class="net-contents">3.4 FL OZ (100 mL)</div>
    </div>
  </div>
  <div class="stage-slot back-slot">
    <div class="label label-back">
      <div class="label-top-bar"></div>
      <div class="back-title">FACE &amp; BEARD LOTION</div>
      <div class="back-rule"></div>
      <div class="back-copy">
        <h3 class="back-heading">DIRECTIONS</h3>
        <p>Massage one pump into face and<br>beard daily. Brush or comb through.<br>Finish with beard oil or balm.</p>
        <h3 class="back-heading">INGREDIENTS</h3>
        <p>Water, Aloe Barbadensis Leaf Juice,<br>Simmondsia Chinensis (Jojoba) Seed<br>Oil, Propanediol, Argania Spinosa<br>Kernel Oil, Panthenol, IBT-50,<br>Niacinamide, Cetyl Alcohol,<br>Phenoxyethanol (and) Caprylyl Glycol.</p>
      </div>
      <div class="maker">BY KESTREL LATHER CO.</div>
      <div class="upc-area"><strong>UPC AREA</strong><span>REPLACE BEFORE PRINT</span></div>
      <div class="web-address">RidgefernBeard.example</div>
    </div>
  </div>
</section>

<div class="accent-bar"></div>
<h1 class="sheet-title">RIDGEFERN</h1>
<p class="sheet-subtitle">FACE &amp; BEARD LOTION &nbsp;/&nbsp; LABEL CONCEPT</p>

<p class="view-tag col-front">FRONT</p>
<p class="view-tag col-back">BACK</p>

<div class="sheet-label col-front">
  <div class="label label-front">
    <div class="label-top-bar"></div>
    <div class="front-art" role="img" aria-label="Illustration of jagged snowy mountain peaks with pine forest"></div>
    <div class="brand-name">Ridgefern<br>Beard Company</div>
    <div class="product-kicker">FACE &amp; BEARD</div>
    <div class="product-name">LOTION</div>
    <div class="variant-band">UNSCENTED</div>
    <div class="key-ingredients">ALOE VERA + NIACINAMIDE<br>+ ARGAN OIL</div>
    <div class="slogan">STAY WILD.<br>STAY BEARDED.</div>
    <div class="net-contents">3.4 FL OZ (100 mL)</div>
  </div>
</div>

<div class="sheet-label col-back">
  <div class="label label-back">
    <div class="label-top-bar"></div>
    <div class="back-title">FACE &amp; BEARD LOTION</div>
    <div class="back-rule"></div>
    <div class="back-copy">
      <h3 class="back-heading">DIRECTIONS</h3>
      <p>Massage one pump into face and<br>beard daily. Brush or comb through.<br>Finish with beard oil or balm.</p>
      <h3 class="back-heading">INGREDIENTS</h3>
      <p>Water, Aloe Barbadensis Leaf Juice,<br>Simmondsia Chinensis (Jojoba) Seed<br>Oil, Propanediol, Argania Spinosa<br>Kernel Oil, Panthenol, IBT-50,<br>Niacinamide, Cetyl Alcohol,<br>Phenoxyethanol (and) Caprylyl Glycol.</p>
    </div>
    <div class="maker">BY KESTREL LATHER CO.</div>
    <div class="upc-area"><strong>UPC AREA</strong><span>REPLACE BEFORE PRINT</span></div>
    <div class="web-address">RidgefernBeard.example</div>
  </div>
</div>

<p class="size-note col-front">1.5 x 2.5 in &nbsp;I&nbsp; shown at 200%</p>
<p class="size-note col-back">1.5 x 2.5 in &nbsp;I&nbsp; shown at 200%</p>

<aside class="notes">
  <h2 class="note-heading">PINE / BONE / BLAZE</h2>
  <p class="note-body">Rugged, modern mountain grooming.</p>

  <h2 class="note-heading" style="margin-top:68px">BUILT AS A SERIES</h2>
  <p class="note-body">Keep the logo zone, bold product title and color band consistent across future beard oils, balms and other grooming products.</p>

  <h2 class="note-heading" style="margin-top:30px">PRINT GEOMETRY</h2>
  <ul class="note-list">
    <li>Trim: 1.5 x 2.5 in</li>
    <li>Bleed: 0.0625 in per side</li>
    <li>PDF page: 1.625 x 2.625 in</li>
    <li>Safe inset: 0.0625 in minimum</li>
    <li>Separate front and back PDFs</li>
  </ul>

  <h2 class="note-heading" style="margin-top:33px">BEFORE PRODUCTION</h2>
  <p class="note-body" style="line-height:14.6px">Replace the temporary logo. Confirm the final ingredient declaration, quantity and company details. Insert the approved UPC in the white panel. Review a printer proof at actual size.</p>
</aside>

<div class="palette" aria-label="Colour palette">
  <div class="swatch pine"></div>
  <div class="swatch bone"></div>
  <div class="swatch blaze"></div>
</div>

<div class="footer-rule"></div>

</body>
</html>
```